Thoroughbred Racing Partnership needs web design

Crest of Fortune Partners is a management group who buys horses and races them on both the West and East coasts. The premise of the business is for an investment as little as $500, anyone can be a partner and own a percentage of a horse(s). This is a low cost way of getting involved in the exciting sport of Thoroughbred Racing, without shouldering the heavy financial responsibility. Our target market is mostly males 40+ but we want to include all target markets. We are looking for something very clean and professional, we want to give an image of success. Nothing overly "artsy." I have included the logo in which you can incorporate in the site. Also, the logo colors will be the colors of our "silks." The silks are what the jockey wears and will be an important marketing tool for COF. We would like a very prominent picture of a racehorse somewhere on the homepage, we want to make it clear that is a website for Horseracing partnerships.

On the top of the site, it should say "Crest of Fortune" (on the top)
and below that "Thoroughbred Racing Partnerships." (below that)

The main sections, which should be across the top are:

Home
About Us
Ownership
Stable Roster
News
Contact us

Some of these will have drop down menus.

An example of a competitor website that we like is: www.harlowfieldeq.example
An example of a competitor website that we don't like is: www.gallopvane.example
Updates

Project Deadline Extended
Reason: We have a Board of Directors meeting on the 22nd and we will be making a decision on that day. I'm giving an extension so that all designers are able to submit their designs by the 22nd. Thank you!

Target Market(s)

40+ males

Industry/Entity Type

Business

Requirements
Must have
• our logo must be on the site. We would like at least one bold image of a thoroughbred horse in action. The picture is going to tell the story so it needs to be very eye-catching.

Our slogan should also be included on the website, "Experience the thrill of owning a Racehorse."
Should not have
• cartoons, artsy pictures, pictures of Steeplechase horses or "jumpers." This partnership is for racehorses only, there is not jumping involved with the horses.

```html
<!DOCTYPE html>
<html lang="en">
<head>
<meta charset="utf-8">
<title>Crest of Fortune Partners</title>
<link href="https://fonts.googleapis.com/css2?family=Arvo:wght@400;700&family=Open+Sans:ital,wght@0,400;0,600;0,700;1,400&display=swap" rel="stylesheet">
<style>
:root{
  --navy:#0e3768;
  --navy-dark:#0a2a52;
  --navy-bar:#1d3b60;
  --ink:#0c2a55;
  --text:#666;
  --muted:#8a8a8a;
  --link:#0b4fa3;
  --quote:#dcdcdc;
  --footer:#9aa1ab;
  --footer-text:#6d7480;
  --white:#fff;
}
*{box-sizing:border-box;margin:0;padding:0}
html,body{width:1108px;height:1200px;overflow:hidden;background:var(--white)}
body{position:relative;font-family:"Open Sans",Arial,sans-serif;color:var(--text)}
.abs{position:absolute}
.site{position:absolute;left:198px;top:0;width:713px;height:1200px}

.topbar{left:0;top:0;width:713px;height:41px;background:linear-gradient(#2a5a92,var(--navy-dark))}
.brand-tab{left:60px;top:0;width:117px;height:72px;z-index:3}
.brand-tab svg{position:absolute;left:0;top:0}
.brand-name{position:absolute;left:0;width:117px;text-align:center;font-family:"Arvo",serif;font-weight:700;color:var(--navy);line-height:1;white-space:nowrap}
.brand-name.big{top:9px;font-size:24px;letter-spacing:1px}
.brand-name.small{top:37px;font-size:10px;letter-spacing:.5px}
.nav{left:304px;top:0;height:41px;display:flex;z-index:2}
.nav a{display:block;height:41px;line-height:40px;padding:0 9px;font-family:"Arvo",serif;font-size:9.5px;color:#c6d3e4;text-decoration:none;border-left:1px solid rgba(255,255,255,.12)}
.nav a:first-child{border-left:0;color:var(--white)}

.hero{left:0;top:41px;width:713px;height:386px;background:linear-gradient(180deg,#e8ebe6 0%,#c9cfc6 35%,#6f5a48 70%,#4c3d2f 100%)}
.hero-caption{left:0;top:290px;width:440px;height:93px;background:rgba(14,55,104,.88)}
.hero-title{position:absolute;left:65px;top:14px;font-family:"Arvo",serif;font-size:38px;color:var(--white);font-variant:small-caps;letter-spacing:-.5px;line-height:1}
.hero-sub{position:absolute;left:70px;top:58px;font-family:"Arvo",serif;font-size:14.5px;color:var(--white)}
.dots{left:336px;top:407px;display:flex;gap:7px}
.dots span{width:6px;height:6px;border-radius:50%;background:rgba(255,255,255,.5)}
.dots span:first-child{background:var(--white)}

.intro-title{left:0;top:446px;width:725px;text-align:center;font-family:"Arvo",serif;font-weight:400;font-size:18.5px;color:var(--ink)}
.intro-text{left:140px;top:475px;width:445px;text-align:center;font-size:10px;line-height:14px;color:var(--muted)}
.intro-text a{color:var(--navy);font-weight:600}

.label{font-family:"Arvo",serif;font-weight:700;font-size:9.5px;color:var(--ink)}
.why{left:78px;top:529px}
.benefits{left:78px;top:553px;list-style:none}
.benefits li{position:relative;padding-left:17px;font-size:12px;line-height:20px;color:#7a7a7a}
.benefits li svg{position:absolute;left:0;top:7px}
.clients{left:494px;top:529px}
.quote{left:494px;top:550px;width:160px;height:70px;background:var(--quote);border-radius:2px;padding:7px 10px;font-style:italic;font-size:7px;line-height:13px;color:#8f8f8f}
.quote-tail{left:506px;top:620px}
.quote-name{left:494px;top:637px;font-size:10px;font-weight:600;color:#666}

.col{top:690px;width:186px}
.col h2{font-family:"Arvo",serif;font-weight:400;font-size:16px;letter-spacing:.5px;color:var(--ink);height:23px}
.col .photo{width:184px;height:117px}
.col p{margin-top:13px;font-size:7.2px;line-height:10.7px;color:#444;padding-left:2px}
.col a{display:inline-block;margin-top:10px;margin-left:2px;font-size:7.5px;font-weight:700;color:var(--link);text-decoration:underline}

.cta{left:0;top:928px;width:713px;height:143px;background:linear-gradient(90deg,#1c1c1c,#3c3a35 45%,#52565c 100%);text-align:center;color:var(--white)}
.cta h3{position:absolute;left:0;top:20px;width:100%;font-family:"Arvo",serif;font-weight:400;font-size:18px}
.cta p{position:absolute;left:160px;top:48px;width:393px;font-size:11px;line-height:13px;color:#c9c9c9}
.cta .call{position:absolute;left:0;top:89px;width:100%;font-size:14px;font-weight:700}
.cta .mail{position:absolute;left:0;top:108px;width:100%;font-size:11px;color:#c9c9c9}

.footer{left:0;top:1071px;width:713px;height:99px;background:var(--footer)}
.footer-brand{position:absolute;left:105px;top:24px;width:110px;text-align:center;font-family:"Arvo",serif;color:#7f8793;line-height:1}
.footer-brand .big{display:block;font-size:26px;font-weight:700;letter-spacing:2px}
.footer-brand .small{display:block;margin-top:4px;font-size:12px;letter-spacing:3px}
.fcol{position:absolute;top:15px;font-family:"Arvo",serif;font-size:7px;line-height:14.3px;color:var(--footer-text)}
.fcol b{display:block;font-weight:400;letter-spacing:.5px;color:#7a818b}
.fcol span{display:block;font-weight:700}
.fcol.contact span{font-family:"Open Sans",sans-serif;font-weight:400}
.legal{left:0;top:1170px;width:713px;height:30px;background:var(--navy-bar);text-align:center;line-height:30px;font-size:7.3px;color:#b9c4d3}
</style>
</head>
<body>
<div class="site">
  <div class="abs topbar"></div>

  <div class="abs hero" role="img" aria-label="Jockeys in coloured silks riding thoroughbreds down the home straight"></div>
  <div class="abs hero-caption">
    <div class="hero-title">Crest of Fortune.</div>
    <div class="hero-sub">Thoroughbred Racing Partnerships.</div>
  </div>
  <div class="abs dots"><span></span><span></span><span></span><span></span></div>

  <div class="abs brand-tab">
    <svg width="117" height="72" viewBox="0 0 117 72"><path d="M0 0H117V60L58.5 72L0 60Z" fill="#fff"/></svg>
    <div class="brand-name big">COF</div>
    <div class="brand-name small">PARTNERS</div>
  </div>
  <nav class="abs nav">
    <a href="#">Home</a><a href="#">About</a><a href="#">Ownership</a><a href="#">Stable Roster</a><a href="#">News</a><a href="#">Contact</a>
  </nav>

  <h1 class="abs intro-title">Experience the Thrill of Owning a Racehorse.</h1>
  <p class="abs intro-text">Crest of Fortune Partners is a management group who buys horses and races them on both the West and East coasts. New to ownership? <a href="#">Learn More</a></p>

  <div class="abs label why">Why Choose COF?</div>
  <ul class="abs benefits">
    <li><svg width="7" height="7" viewBox="0 0 7 7"><path d="M0 3.5H6M3.5 1L6 3.5L3.5 6" stroke="#0e3768" stroke-width="1.3" fill="none"/></svg>Anyone can be a partner and own a percentage of a horse(s)</li>
    <li><svg width="7" height="7" viewBox="0 0 7 7"><path d="M0 3.5H6M3.5 1L6 3.5L3.5 6" stroke="#0e3768" stroke-width="1.3" fill="none"/></svg>Low cost way of getting involved .</li>
    <li><svg width="7" height="7" viewBox="0 0 7 7"><path d="M0 3.5H6M3.5 1L6 3.5L3.5 6" stroke="#0e3768" stroke-width="1.3" fill="none"/></svg>No shouldering the heavy financial responsibility.</li>
    <li><svg width="7" height="7" viewBox="0 0 7 7"><path d="M0 3.5H6M3.5 1L6 3.5L3.5 6" stroke="#0e3768" stroke-width="1.3" fill="none"/></svg>We give our Partners access to a level of the game.</li>
    <li><svg width="7" height="7" viewBox="0 0 7 7"><path d="M0 3.5H6M3.5 1L6 3.5L3.5 6" stroke="#0e3768" stroke-width="1.3" fill="none"/></svg>The premise of the business is for an investment as little as $500</li>
  </ul>

  <div class="abs label clients">What Our Client’s Say ?</div>
  <blockquote class="abs quote">Curabitur quis nisl in leo euismod venenatis eu in diam. Etiam auctor diam pellentesque lectus vehicula mattis. Nulla ac massa at dolor condimentum</blockquote>
  <svg class="abs quote-tail" width="14" height="14" viewBox="0 0 14 14"><path d="M0 0H14L14 14Z" fill="#dcdcdc"/></svg>
  <div class="abs quote-name">Jhon Doe, Company XYZ</div>

  <section class="abs col" style="left:78px">
    <h2>ABOUT COF</h2>
    <div class="photo" role="img" aria-label="Racehorse and jockey at full gallop past the rail" style="background:linear-gradient(135deg,#c9c2a8,#3a2a20 55%,#c9a94a)"></div>
    <p>Lorem ipsum dolor sit amet, consectetur adipisicing elit, sed do eiusmod tempor incididunt ut labore et dolore magna aliqua. Ut enim ad minim veniam, quis nostrud exercitation.</p>
    <a href="#">READ MORE</a>
  </section>
  <section class="abs col" style="left:275px">
    <h2>OWNERSHIP</h2>
    <div class="photo" role="img" aria-label="Close view of a chestnut racehorse in stride" style="background:linear-gradient(135deg,#7a3a1c,#b8662e 50%,#4a2414)"></div>
    <p>Lorem ipsum dolor sit amet, consectetur adipisicing elit, sed do eiusmod tempor incididunt ut labore et dolore magna aliqua. Ut enim ad minim veniam, quis nostrud exercitation.</p>
    <a href="#">READ MORE</a>
  </section>
  <section class="abs col" style="left:465px">
    <h2>LATEST NEWS</h2>
    <div class="photo" role="img" aria-label="Partners presenting a framed award at a racing event" style="background:linear-gradient(135deg,#2a2a2a,#5b6170 50%,#1d2330)"></div>
    <p>Lorem ipsum dolor sit amet, consectetur adipisicing elit, sed do eiusmod tempor incididunt ut labore et dolore magna aliqua. Ut enim ad minim veniam, quis nostrud exercitation.</p>
    <a href="#">READ MORE</a>
  </section>

  <div class="abs cta" role="img" aria-label="Blurred racing scene behind the call to action">
    <h3>Want to partner with us?</h3>
    <p>Capacitance cascading integer reflective interface data development high bus cache dithering transponder.</p>
    <div class="call">CALL US TODAY +1800 123 4567</div>
    <div class="mail">email us: info@cof.example</div>
  </div>

  <footer class="abs footer">
    <div class="footer-brand"><span class="big">COF</span><span class="small">PARTNERS</span></div>
    <div class="fcol" style="left:264px"><b>NAVIGATION</b><span>Home</span><span>Ownership</span><span>Stable Roster</span></div>
    <div class="fcol" style="left:375px"><b>ABOUT US</b><span>About</span><span>News</span><span>Contact Us</span></div>
    <div class="fcol contact" style="left:482px"><b>CONTACT US</b><span>Phone : +61 3 123 5467</span><span>Email: info@cof.example</span><span>Your Street, Your Avenue</span><span>Your Country, 10001</span></div>
  </footer>
  <div class="abs legal">© Copyright 2013 COF PARTNERS. All Right Reserved | Privacy Policy | Site Map</div>
</div>
</body>
</html>
```